Create Lanternfield HR Business Cards.

Create Business Cards for Lanternfield HR. 2 sided and Would like the back to have the logo.

Info for Business Card:
Address: 4827 Millbrook Ave Suite 230 Cleveland, Ohio 44987
Office Number: 216-555-0143
Mobile: 216-555-0192

Website: www.lanternfieldhr.example

Target Market(s)

Small to medium size businesses

Industry/Entity Type

Human Resources

Contact Information for Business Card

Company logo and information

Font styles to use
Serif
Sans Serif

Requirements
Must have
• Info for Business Card: Address: 4827 Millbrook Ave Suite 230 Cleveland, Ohio 44987 Office Number: 216-555-0143 Mobile: 216-555-0192 Website: www.lanternfieldhr.example

```html
<!DOCTYPE html>
<html lang="en">
<head>
<meta charset="utf-8">
<title>Lanternfield HR – Business Cards</title>
<link rel="stylesheet" href="https://fonts.googleapis.com/css2?family=Arimo:wght@400;700&display=swap">
<style>
  :root {
    --navy: #2b2563;
    --orange: #f28a24;
    --peach: #fdebdf;
    --mist: #e1e0e9;
    --paper: #ffffff;
    --backdrop: #ece4da;
  }
  * { margin: 0; padding: 0; box-sizing: border-box; }
  html, body {
    width: 1200px; height: 1200px; overflow: hidden;
    background: var(--backdrop);
    font-family: "Arimo", Arial, sans-serif;
  }
  .sheet { position: relative; width: 1200px; height: 1200px; }
  .card {
    position: absolute; left: 165px; width: 870px; height: 509px;
    background: var(--paper); overflow: hidden;
  }
  .card--front { top: 66px; }
  .card--back { top: 625px; }

  .accent-band {
    position: absolute; top: 0; right: 0; width: 330px; height: 22px;
    background: var(--peach);
  }
  .accent-rule {
    position: absolute; top: 34px; right: 0; width: 200px; height: 4px;
    background: var(--mist);
  }

  .brand {
    position: absolute; display: flex; align-items: center; gap: 14px;
    color: var(--navy); font-weight: 700; letter-spacing: 0.5px;
  }
  .brand__dot { border-radius: 50%; background: var(--orange); flex: none; }
  .card--front .brand { left: 85px; top: 150px; font-size: 40px; }
  .card--front .brand__dot { width: 40px; height: 40px; }
  .card--back .brand {
    left: 0; right: 0; top: 0; bottom: 0; justify-content: center;
    font-size: 50px;
  }
  .card--back .brand__dot { width: 50px; height: 50px; }

  .contact {
    position: absolute; right: 65px; top: 310px;
    list-style: none; text-align: right;
  }
  .contact__item {
    display: flex; justify-content: flex-end; align-items: center;
    gap: 16px; height: 40px; font-size: 20px; color: var(--navy);
  }
  .contact__item--web { color: var(--orange); font-weight: 700; }
  .contact__icon { width: 18px; height: 18px; flex: none; }
</style>
</head>
<body>
<main class="sheet">
  <section class="card card--front" aria-label="Card front">
    <div class="accent-band" aria-hidden="true"></div>
    <div class="accent-rule" aria-hidden="true"></div>
    <div class="brand"><span class="brand__dot"></span><span class="brand__name">Lanternfield HR</span></div>
    <ul class="contact">
      <li class="contact__item">216-555-0143
        <svg class="contact__icon" viewBox="0 0 24 24" aria-label="Office"><path fill="var(--navy)" d="M6.6 10.8a15 15 0 0 0 6.6 6.6l2.2-2.2c.3-.3.7-.4 1-.2 1.1.4 2.3.6 3.6.6.6 0 1 .4 1 1V20c0 .6-.4 1-1 1A17 17 0 0 1 3 4c0-.6.4-1 1-1h3.5c.6 0 1 .4 1 1 0 1.3.2 2.5.6 3.6.1.3 0 .7-.2 1z"/></svg>
      </li>
      <li class="contact__item">216-555-0192
        <svg class="contact__icon" viewBox="0 0 24 24" aria-label="Mobile"><rect x="6" y="2" width="12" height="20" rx="2" fill="none" stroke="var(--navy)" stroke-width="2"/><circle cx="12" cy="18" r="1.2" fill="var(--navy)"/></svg>
      </li>
      <li class="contact__item contact__item--web">www.lanternfieldhr.example
        <svg class="contact__icon" viewBox="0 0 24 24" aria-label="Website"><circle cx="12" cy="12" r="10" fill="var(--orange)"/><path d="M2 12h20M12 2c3 3 3 17 0 20M12 2c-3 3-3 17 0 20M4 7h16M4 17h16" stroke="#fff" stroke-width="1.3" fill="none"/></svg>
      </li>
      <li class="contact__item">4827 Millbrook Ave Suite 230 Cleveland, Ohio 44987
        <svg class="contact__icon" viewBox="0 0 24 24" aria-label="Address"><path fill="var(--navy)" d="M12 2a7 7 0 0 0-7 7c0 5 7 13 7 13s7-8 7-13a7 7 0 0 0-7-7zm0 9.5A2.5 2.5 0 1 1 12 6.5a2.5 2.5 0 0 1 0 5z"/></svg>
      </li>
    </ul>
  </section>

  <section class="card card--back" aria-label="Card back">
    <div class="brand"><span class="brand__dot"></span><span class="brand__name">Lanternfield HR</span></div>
  </section>
</main>
</body>
</html>
```